Website design for luxury private hair salon

I'm looking for someone to use my Logo and build me a website for my webpage www.lunetresses.com.au (You can have a look at it as it has every detail I need included on it already), however I want a fresh new appearance and it to look and feel super stylish.

I am thinking colours in black, with silver or white, beautiful hair images like the ones you'll see on the current webpage - the price list as per what you already see.

I will include a copy of my biz card on here, so you can see the feel of the card, and design a website with a similar feel. It is matt black with a foil silver.

Modern, but classic and fresh. I will also need you to be able to publish it to my URL for me as I have no idea how to do this. I need it up and running pronto!

The website will need to be able to be read clearly on all devices incluing smart phones and ipads. The URL is currently registered and hosted by Nimbo Vault

Thinking a Home Page - large logo etc and write up on who and what we offer
Services/Price List page - as per the price list on my current webpage
Contact Page - with a built in contact form.

Target Market(s)

Middle aged, fashionable, stylish women and men who enjoy luxury hair care and styling in an upmarket location.

Industry/Entity Type

Hair And Beauty

Number of Pages Required

3 page

Font styles to use
Other font styles liked:
• see my images for my current logo

Colors
000000
b2b2b2
a54499

Requirements
Must have
• Style
• Fast turnaround
• Be viewable on all devices, PC, ipads, smart phones
• Designer able to upload it so its a running website for me to my URL
Nice to have
• Just a really feminine, stylish website which is easy to read and shows some beautiful images of perfect hair
Should not have
• Browns, reds or orange colours.

```html
<!DOCTYPE html>
<html lang="en">
<head>
<meta charset="utf-8">
<title>Lune hair &amp; body</title>
<link rel="stylesheet" href="https://fonts.googleapis.com/css2?family=Jost:wght@300;400&display=swap">
<style>
:root{
  --purple:#a54499;
  --purple-soft:#b868ad;
  --ink:#333333;
  --grey-text:#7a7a7a;
  --silver:#b2b2b2;
  --contact-bg:#a3a3a3;
  --footer-bg:#2f2f2f;
  --white:#ffffff;
}
*{margin:0;padding:0;box-sizing:border-box}
html,body{width:770px;height:1200px;overflow:hidden;background:var(--white)}
body{font-family:"Jost",Arial,sans-serif;font-weight:400;color:var(--ink);position:relative}
.abs{position:absolute}
/* header */
.site-header{left:0;top:0;width:770px;height:65px;background:var(--white)}
.brand{left:14px;top:8px;color:#8a8a8a;font-size:34px;line-height:1;font-weight:300;letter-spacing:1px}
.brand small{font-size:12px;letter-spacing:1px;margin-left:4px}
.main-nav{right:28px;top:28px;font-size:16px;color:var(--purple);letter-spacing:.3px;white-space:nowrap}
.main-nav span{margin:0 7px}
/* hero */
.hero{left:0;top:65px;width:770px;height:370px;
  background:radial-gradient(circle at 70% 15%,#f6dca0 0%,#d9b87a 18%,rgba(120,110,80,.6) 45%,transparent 70%),
  linear-gradient(180deg,#6f6a4a 0%,#4c4a38 45%,#2f2e33 100%)}
.hero-brand{left:30px;top:130px;color:var(--white);font-weight:300;line-height:1}
.hero-brand .name{font-size:120px;letter-spacing:2px}
.hero-brand .tag{display:block;font-size:30px;letter-spacing:2px;margin:8px 0 0 124px}
/* who we are */
.section-title{width:770px;left:0;text-align:center;font-size:19px;letter-spacing:.5px;color:var(--ink)}
.who-quote{left:90px;top:474px;width:590px;text-align:center;font-size:13.5px;line-height:17px;color:var(--grey-text)}
/* services */
.services{left:0;top:548px;width:770px;height:165px;
  background:linear-gradient(90deg,#c98fbf 0%,#b66fab 40%,#a54499 100%)}
.services .section-title{color:var(--white);top:17px}
.service-list{list-style:none;color:var(--white);font-size:14.5px}
.service-list li{height:32px;line-height:32px}
.service-list li::before{content:"";display:inline-block;width:6px;height:6px;border-radius:50%;background:var(--white);margin-right:10px;vertical-align:middle}
/* review */
.review-intro{left:0;width:770px;top:747px;text-align:center;font-size:13.5px;color:var(--grey-text)}
.rating-list{left:126px;top:770px;list-style:none;font-size:11px;color:var(--grey-text)}
.rating-list li{height:18px;line-height:18px}
.rating-list li::before{content:"";display:inline-block;width:12px;height:12px;border-radius:50%;background:var(--purple);margin-right:22px;vertical-align:middle}
.referral{left:0;width:770px;top:832px;text-align:center;font-size:11px;color:var(--purple)}
/* contact */
.contact{left:0;top:858px;width:770px;height:213px;background:var(--contact-bg)}
.contact .section-title{top:7px;font-size:19px;color:#222}
.field{background:var(--white);border:1px solid #ccc;font-size:8px;color:#888;padding:9px 10px;font-family:Arial,sans-serif}
.send-btn{left:341px;top:167px;width:107px;height:29px;background:var(--purple);color:var(--white);font-size:15px;text-align:center;line-height:29px}
/* footer */
.site-footer{left:0;top:1071px;width:770px;height:129px;background:var(--footer-bg)}
.footer-brand{left:14px;top:16px;color:var(--silver);font-size:32px;font-weight:300;line-height:1}
.footer-brand small{font-size:11px;margin-left:4px}
.copyright{left:10px;top:102px;font-size:12.5px;color:var(--silver)}
.footer-label{font-size:12.5px;color:var(--purple);letter-spacing:.5px}
.footer-info{font-size:12.5px;color:#cfcfcf;letter-spacing:.5px;line-height:20px}
.social{left:600px;top:48px;display:flex;gap:12px}
.social span{width:36px;height:36px;border-radius:50%;background:var(--purple-soft);display:block}
</style>
</head>
<body>
<header class="abs site-header">
  <div class="abs brand">Lune<small>hair &amp; body</small></div>
  <nav class="abs main-nav">HOME<span>I</span>WHO WE ARE<span>I</span>PRICE LISTS<span>I</span>CONTACT US</nav>
</header>

<div class="abs hero" role="img" aria-label="Photograph of a woman with long blonde hair sitting by a lake at sunset"></div>
<div class="abs hero-brand"><span class="name">Lune</span><span class="tag">hair &amp; body</span></div>

<h2 class="abs section-title" style="top:447px">WHO WE ARE</h2>
<p class="abs who-quote">"We pride ourselves on being able to offer a private salon experience to our clients in the exclusive suburb of Halden Bay, where your hair design and colouring needs will be met with years of experience and current industry training and knowledge". &nbsp;- &nbsp;The Lune Team</p>

<section class="abs services" role="img" aria-label="Soft purple-toned photograph of a woman with flowing hair behind the services list">
  <h2 class="abs section-title">OUR SERVICES</h2>
  <ul class="abs service-list" style="left:86px;top:52px"><li>Hair Cuts</li><li>Colouring</li><li>Highlighting</li></ul>
  <ul class="abs service-list" style="left:332px;top:52px"><li>Extensions</li><li>Straightening</li><li>Bridal</li></ul>
  <ul class="abs service-list" style="left:566px;top:51px"><li>Treatments</li><li>Products &amp; Advice</li></ul>
</section>

<h2 class="abs section-title" style="top:720px">REVIEW US</h2>
<p class="abs review-intro">If you'd like to just leave us a quick review - rating your last experience with us from 1 - 3, that would be great!</p>
<ul class="abs rating-list">
  <li>1 - You think we are amazing and love the services we provide &amp; will be a loyal client FOREVER!</li>
  <li>2 - You were happy with the service but feel there were areas we could improve?</li>
  <li>3 - It was a below average experience and you won't be returning :-(</li>
</ul>
<p class="abs referral">RECOMMENDATION - One of our loyal clients has referred you to us? You'll both receive 10% off your next appointment.</p>

<section class="abs contact" role="img" aria-label="Faint world map pattern on grey behind the contact form">
  <h2 class="abs section-title">CONTACT US</h2>
  <div class="abs field" style="left:82px;top:40px;width:297px;height:30px">Your Name *</div>
  <div class="abs field" style="left:82px;top:82px;width:297px;height:30px">Your Email *</div>
  <div class="abs field" style="left:82px;top:125px;width:297px;height:30px">Your Phone *</div>
  <div class="abs field" style="left:395px;top:40px;width:297px;height:115px">Your Message *</div>
  <div class="abs send-btn">Send Message</div>
</section>

<footer class="abs site-footer">
  <div class="abs footer-brand">Lune<small>hair &amp; body</small></div>
  <p class="abs copyright">Copyright © &nbsp;www.lunetresses.com.au - 2017.</p>
  <p class="abs footer-label" style="left:294px;top:16px">WE ARE LOCATED AT:</p>
  <p class="abs footer-info" style="left:296px;top:34px">HALDEN BAY, &nbsp;Western Australia - 6099</p>
  <p class="abs footer-label" style="left:294px;top:63px">CALL US FOR APPOINTMENT :</p>
  <p class="abs footer-info" style="left:296px;top:82px">TARA &nbsp;0400 555 218<br>NINA &nbsp;0411 555 947</p>
  <p class="abs footer-label" style="left:636px;top:16px">FOLLOW US:</p>
  <div class="abs social" aria-label="Social links: Facely, Chirpa, Orbit"><span></span><span></span><span></span></div>
</footer>
</body>
</html>
```